Newly established winery needs label for its bottles

The Corvel-Tamarin Winery, is a small family owned winery that has been producing wine for little over 3 years. We are now ready to officially start commercializing our products. To do so we are looking for a label for our wine bottles. We are looking for a creative design that will differentiate our bottles from the more conventional labels. We are looking for one label design with 3 color schemes so that we can have a standard look and feel for all three of our wines, while having some differentiation between them with the different color schemes. In summary we are looking for a label that will standout by its uniqueness, simplicity and its modern touch. The label should also reflect the historical significance of the name of the winery. The attached documents offers more detail about the winery, what we are looking for, as well as some technical specification for the label. This label project is also related to a logo project see brief: http://www.pitchvault.ca/project-progress.aspx?briefId=462193). The logo project is now complete and the winning design source files were added to the documents in this brief. Also, details around the information that will need to appear on the label was added to the document list.
Updates
This label project will be on hold temporarily while the logo project is in progress. If you are interested in participating in the logo project, please follow this link: http://www.pitchvault.ca/project-progress.aspx?briefId=462193 Added Wednesday, December 17, 2014
Reason: Deadline extended to give sufficent time for submission and modification to the designs provided.

```html
<!DOCTYPE html>
<html lang="fr">
<head>
<meta charset="utf-8">
<title>Corvel Tamarin — Wine Labels</title>
<link rel="stylesheet" href="https://fonts.googleapis.com/css2?family=EB+Garamond:wght@400;600&display=swap">
<style>
  :root {
    --page: #ffffff;
    --gold: #f0c85a;
    --silver: #c9c9c9;
    --muted: #9a9a9a;
    --rouge-edge: #262626;
    --rouge-mid: #4c4c4c;
    --blanc-edge: #231a1c;
    --blanc-mid: #433034;
    --rose-edge: #0a0a08;
    --rose-mid: #1f1f21;
  }
  * { margin: 0; padding: 0; box-sizing: border-box; }
  html, body { width: 1200px; height: 1000px; overflow: hidden; background: var(--page); }
  .canvas {
    position: relative; width: 1200px; height: 1000px;
    font-family: "EB Garamond", "Times New Roman", serif;
  }
  .label {
    position: absolute; top: 318px; width: 266px; height: 468px;
    display: flex; flex-direction: column; align-items: center;
    padding-top: 30px;
  }
  .label--rouge { left: 160px; background: linear-gradient(90deg, var(--rouge-edge), var(--rouge-mid) 45%, var(--rouge-edge)); }
  .label--blanc { left: 468px; background: linear-gradient(90deg, var(--blanc-edge), var(--blanc-mid) 55%, var(--blanc-edge)); }
  .label--rose  { left: 777px; background: linear-gradient(90deg, var(--rose-edge), var(--rose-mid) 50%, var(--rose-edge)); }
  .origin { color: var(--gold); font-size: 11px; line-height: 1; }
  .type-fr { color: var(--silver); font-size: 19px; letter-spacing: 0.5px; margin-top: 5px; }
  .brand {
    margin-top: 58px; display: flex; align-items: center; gap: 10px;
    color: var(--gold); font-weight: 600; font-size: 26px; letter-spacing: 1px;
    text-transform: uppercase; height: 80px;
  }
  .brand-dot { width: 14px; height: 14px; border-radius: 50%; background: var(--gold); }
  .type-en { color: var(--silver); font-size: 19px; margin-top: 62px; letter-spacing: 0.5px; }
  .origin-en { color: var(--gold); font-size: 11px; line-height: 1; }
  .vintage { color: var(--gold); font-size: 27px; margin-top: 38px; }
  .specs {
    position: absolute; left: 18px; right: 16px; bottom: 22px;
    display: flex; justify-content: space-between;
    color: var(--muted); font-size: 13px;
  }
</style>
</head>
<body>
<main class="canvas">
  <section class="label label--rouge">
    <p class="origin">Produit du Québec</p>
    <h2 class="type-fr">VIN ROUGE</h2>
    <div class="brand"><span class="brand-dot"></span>Corvel Tamarin</div>
    <h3 class="type-en">RED WINE</h3>
    <p class="origin-en">Product of Québec</p>
    <p class="vintage">2012</p>
    <div class="specs"><span>11,7 % alc./vol</span><span>750 ml</span></div>
  </section>

  <section class="label label--blanc">
    <p class="origin">Produit du Québec</p>
    <h2 class="type-fr">VIN BLANC</h2>
    <div class="brand"><span class="brand-dot"></span>Corvel Tamarin</div>
    <h3 class="type-en">WHITE WINE</h3>
    <p class="origin-en">Product of Québec</p>
    <p class="vintage">2013</p>
    <div class="specs"><span>12,6 % alc./vol</span><span>750 ml</span></div>
  </section>

  <section class="label label--rose">
    <p class="origin">Produit du Québec</p>
    <h2 class="type-fr">VIN ROSÉ</h2>
    <div class="brand"><span class="brand-dot"></span>Corvel Tamarin</div>
    <h3 class="type-en">ROSÉ WINE</h3>
    <p class="origin-en">Product of Québec</p>
    <p class="vintage">2013</p>
    <div class="specs"><span>13,8 % alc./vol</span><span>750 ml</span></div>
  </section>
</main>
</body>
</html>
```